ashby paving works

Needs to have phone number 0412885107 and email marklowry@pavemail.com.au.
ABN 27613048852
name mark lowry

For all your concreting solutions
Excavation
Exposed & colour concrete
House & shed slabs
Driveways
Landing & steps

Contact Information for Business Card

ph 0412885107
email marklowry@pavemail.com.au.
ABN 27613048852
name mark lowry

```html
<!DOCTYPE html>
<html lang="en">
<head>
<meta charset="utf-8">
<title>Ashby Paving Works – Business Card</title>
<link rel="stylesheet" href="https://fonts.googleapis.com/css2?family=Montserrat:wght@300;400;600;800&display=swap">
<style>
  :root {
    --orange: #f06a24;
    --orange-light: #f7a033;
    --grey-text: #6b6b6b;
    --grey-dark: #5a5a5a;
    --white: #ffffff;
    --backdrop: #2b2b2b;
  }
  * { box-sizing: border-box; margin: 0; padding: 0; }
  html, body { width: 1200px; height: 1200px; overflow: hidden; }
  body {
    background: var(--backdrop);
    font-family: "Montserrat", sans-serif;
    display: flex;
    flex-direction: column;
    align-items: center;
    justify-content: center;
    gap: 60px;
  }
  .card {
    width: 900px;
    height: 514px;
    background: var(--white);
    position: relative;
    overflow: hidden;
    box-shadow: 0 10px 30px rgba(0,0,0,.4);
  }

  /* Back of card */
  .card-back .phone-band {
    height: 220px;
    background: var(--orange);
    display: flex;
    flex-direction: column;
    align-items: center;
    justify-content: center;
    gap: 14px;
    color: var(--white);
  }
  .phone-row {
    display: flex;
    align-items: center;
    gap: 22px;
  }
  .phone-row .rule {
    width: 110px;
    height: 2px;
    background: var(--white);
  }
  .phone-number {
    font-weight: 400;
    font-size: 46px;
    letter-spacing: 4px;
  }
  .services {
    padding: 44px 0 0 96px;
  }
  .tagline {
    font-weight: 800;
    font-size: 34px;
    color: var(--grey-dark);
    letter-spacing: 1px;
    margin-bottom: 12px;
  }
  .service-list { list-style: none; }
  .service-list li {
    font-weight: 400;
    font-size: 29px;
    color: var(--grey-text);
    line-height: 35px;
    letter-spacing: 1px;
    display: flex;
    align-items: center;
    gap: 22px;
  }
  .service-list li::before {
    content: "";
    width: 14px;
    height: 12px;
    background: var(--orange);
    flex: none;
  }

  /* Front of card */
  .card-front { display: flex; }
  .brand-side {
    width: 50%;
    display: flex;
    align-items: center;
    justify-content: center;
    gap: 16px;
  }
  .brand-mark {
    width: 26px;
    height: 26px;
    background: var(--orange);
  }
  .brand-name {
    font-weight: 600;
    font-size: 28px;
    color: var(--orange);
    text-transform: uppercase;
    letter-spacing: 0.5px;
  }
  .contact-side {
    width: 50%;
    background: radial-gradient(circle at 0% 0%, var(--orange-light) 0%, var(--orange) 45%);
    color: var(--white);
    display: flex;
    flex-direction: column;
    align-items: center;
    justify-content: center;
    text-align: center;
  }
  .person-name {
    font-weight: 800;
    font-size: 40px;
    letter-spacing: 1.5px;
    margin-bottom: 56px;
  }
  .contact-line {
    font-weight: 400;
    font-size: 20px;
    letter-spacing: 0.5px;
    line-height: 34px;
  }
  .contact-line.abn { font-size: 26px; margin-bottom: 30px; }
  .contact-side .phone-row .rule { width: 70px; }
  .contact-side .phone-number { font-size: 34px; letter-spacing: 3px; margin-top: 10px; }
</style>
</head>
<body>

<section class="card card-back">
  <div class="phone-band">
    <div class="phone-row">
      <span class="rule"></span>
      <svg class="phone-icon" width="78" height="78" viewBox="0 0 78 78" aria-hidden="true">
        <circle cx="39" cy="39" r="35" fill="none" stroke="#fff" stroke-width="4"/>
        <path d="M27 22c2-2 5-2 6 1l3 7c1 2 0 4-2 5l-2 1c2 5 6 9 11 11l1-2c1-2 3-3 5-2l7 3c3 1 3 4 1 6l-3 3c-3 3-9 2-16-3s-12-12-14-18c-1-4 0-8 3-12z" fill="#fff"/>
      </svg>
      <span class="rule"></span>
    </div>
    <div class="phone-number">0412885107</div>
  </div>
  <div class="services">
    <h2 class="tagline">For all your concreting solutions</h2>
    <ul class="service-list">
      <li>Excavation</li>
      <li>Exposed &amp; colour concrete</li>
      <li>House &amp; shed slabs</li>
      <li>Driveways</li>
      <li>Landing &amp; steps</li>
    </ul>
  </div>
</section>

<section class="card card-front">
  <div class="brand-side">
    <span class="brand-mark"></span>
    <span class="brand-name">Ashby Paving Works</span>
  </div>
  <div class="contact-side">
    <h1 class="person-name">Mark Lowry</h1>
    <p class="contact-line email">marklowry@pavemail.com.au.</p>
    <p class="contact-line abn">ABN 27613048852</p>
    <div class="phone-row">
      <span class="rule"></span>
      <svg class="phone-icon" width="60" height="60" viewBox="0 0 78 78" aria-hidden="true">
        <circle cx="39" cy="39" r="35" fill="none" stroke="#fff" stroke-width="4"/>
        <path d="M27 22c2-2 5-2 6 1l3 7c1 2 0 4-2 5l-2 1c2 5 6 9 11 11l1-2c1-2 3-3 5-2l7 3c3 1 3 4 1 6l-3 3c-3 3-9 2-16-3s-12-12-14-18c-1-4 0-8 3-12z" fill="#fff"/>
      </svg>
      <span class="rule"></span>
    </div>
    <div class="phone-number">0412885107</div>
  </div>
</section>

</body>
</html>
```